Web Design for Harbor Link Guild

We need a web design for Harbor Link Guild. You can see more details about the kind of business that it deals with in this link: http://harborlinkguild.ae/. The concept of the site is similar to http://www.travimo.com/ and we are looking for a homepage design also similar to it.
The top navigation should have:
1) directory
2) articles
3) deals
4) forums
5) log in/register page.
It should also have a video, a slider, map & text as well as a call to action to a "why register page".
As part of the footer it should include:
1) about HLG
2) contact HGL
3) terms & conditions
4) privacy
The color palette for the site will be the UAE flag colors which are red, green, white and black.
Updates
Project Deadline Extended
Reason: We need more designs and options.
Keep sending in more creative designs. thanks.
Industry/Entity Type
Business
Look and feel
Each slider illustrates characteristics of the customer's brand and the style your logo design should communicate.

```html
<!DOCTYPE html>
<html lang="en">
<head>
<meta charset="utf-8">
<title>Harbor Link Guild — Home</title>
<link href="https://fonts.googleapis.com/css2?family=Open+Sans:wght@400;600;700&display=swap" rel="stylesheet">
<style>
:root{
  --red:#d7262f;
  --green:#1f9a4a;
  --green-dark:#137a37;
  --black:#1b1b1b;
  --charcoal:#2b2b2b;
  --footer:#262626;
  --grey:#eceeef;
  --grey-mid:#c9cdd0;
  --text:#4a4a4a;
  --muted:#8a8a8a;
  --white:#ffffff;
}
*{box-sizing:border-box;margin:0;padding:0}
html,body{width:824px;height:1200px;overflow:hidden;background:var(--white)}
body{font-family:"Open Sans",Arial,sans-serif;color:var(--text);font-size:11px;line-height:1.5}
.page{width:824px;height:1200px;position:relative}

.topstrip{height:11px;background:var(--red)}
.header{height:66px;display:flex;align-items:center;justify-content:space-between;padding:0 20px;border-bottom:1px solid #e3e3e3;position:relative}
.brand{display:flex;align-items:center;gap:8px;font-weight:700;font-size:22px;color:var(--red);letter-spacing:.5px}
.brand-mark{width:22px;height:22px;background:var(--green);border-radius:50%}
.header-contact{position:absolute;right:20px;top:-11px;height:11px;display:flex;gap:12px;align-items:center;font-size:7.5px;line-height:11px;color:var(--white)}
.member-login{background:var(--black);color:var(--white);font-size:7.5px;font-weight:700;padding:0 8px;height:15px;line-height:15px;align-self:flex-start}
.nav{display:flex;height:66px;align-items:stretch}
.nav a{display:flex;align-items:center;padding:0 12px;color:var(--charcoal);text-decoration:none;font-size:11.5px;font-weight:600}
.nav a.active{background:var(--green);color:var(--white)}
.nav a.register{color:var(--red)}

.hero{height:335px;background:linear-gradient(180deg,#f4f5f6,#dfe2e4);display:flex;padding:32px 20px 0;gap:28px}
.video{width:420px;height:270px;background:linear-gradient(135deg,#d8dcdf,#9aa2a8);position:relative;border:4px solid var(--white);box-shadow:0 2px 6px rgba(0,0,0,.2)}
.video-play{position:absolute;left:50%;top:45%;transform:translate(-50%,-50%);width:76px;height:52px;background:rgba(20,20,20,.85);border-radius:10px}
.video-play svg{position:absolute;left:28px;top:14px}
.video-bar{position:absolute;left:0;right:0;bottom:0;height:26px;background:var(--black);display:flex;align-items:center;padding:0 10px;gap:8px}
.video-bar .track{flex:1;height:4px;background:#555}
.video-bar .track span{display:block;width:30%;height:4px;background:var(--red)}
.hero-copy{flex:1;padding-top:4px}
.project{display:flex;align-items:center;gap:10px;margin-bottom:24px}
.project-badge{width:40px;height:40px;border-radius:50%;background:#c7a44a}
.project-name{font-size:13px;font-weight:700;color:var(--red);line-height:1.3}
.hero-copy p{font-size:15px;color:var(--charcoal);line-height:1.45;margin-bottom:22px}
.btn-register{display:block;width:190px;margin-left:50px;background:var(--green);color:var(--white);text-align:center;font-weight:700;font-size:16px;padding:10px 0;text-decoration:none;border-bottom:3px solid var(--green-dark)}

.welcome{height:288px;display:flex;padding:28px 20px 0;gap:30px}
.welcome-text{width:430px}
.welcome h2{font-size:20px;color:var(--black);font-weight:600;margin-bottom:8px}
.welcome p{font-size:10.5px;margin-bottom:10px;color:var(--text)}
.read-more{color:var(--red);font-size:10.5px;text-decoration:none}
.welcome-art{flex:1;height:230px;margin-left:20px;border-radius:6px;background:linear-gradient(135deg,#f1f2f3 0%,#e3e6e8 55%,#d5d9dc 100%)}

.testimonials{height:175px;background:var(--grey);text-align:center;padding-top:16px}
.testimonials h3{font-size:15px;font-weight:600;color:var(--charcoal);margin-bottom:14px}
.quote{width:600px;margin:0 auto;font-size:10px;color:var(--muted);line-height:1.55}
.client{margin-top:12px;font-size:10.5px;color:var(--charcoal);font-weight:600}
.client span{display:block;font-weight:400;font-size:9px;color:var(--muted)}

.partners{height:87px;display:flex;justify-content:space-around;align-items:center;padding:0 14px;border-bottom:1px solid #e3e3e3}
.partner{display:flex;align-items:center;gap:5px;font-size:11px;font-weight:600;color:var(--charcoal)}
.partner i{width:12px;height:12px;background:var(--grey-mid);display:block}

.footer{height:188px;background:var(--footer);margin-top:10px;display:flex;padding:16px 20px 0;gap:40px;color:#bdbdbd}
.footer h4{color:var(--white);font-size:12px;font-weight:600;margin-bottom:8px}
.footer-col{font-size:9.5px;line-height:1.5}
.tweet{width:260px}
.tweet a,.articles a{color:var(--green);text-decoration:none}
.articles{width:270px}
.article{margin-bottom:10px}
.article strong{color:var(--white);font-weight:600;display:block}
.contact{flex:1;font-size:11px}
.contact p{margin-bottom:6px}
.contact svg{vertical-align:middle;margin-right:6px}
.socials{display:flex;gap:6px;margin-top:6px}
.socials i{width:20px;height:20px;display:block;background:#4a4a4a}
.bottom-bar{height:28px;background:var(--black);display:flex;justify-content:space-between;align-items:center;padding:0 20px;font-size:9px;color:#9a9a9a}
.bottom-bar nav a{color:#cfcfcf;text-decoration:none;margin-left:4px}
</style>
</head>
<body>
<div class="page">
  <div class="topstrip"></div>
  <header class="header">
    <div class="header-contact"><span>+971 (4) 555 0188</span><span>info@harborlinkguild.ae</span><span class="member-login">MEMBER LOGIN</span></div>
    <div class="brand"><span class="brand-mark"></span>HARBOR LINK GUILD</div>
    <nav class="nav">
      <a class="active" href="#">Home</a>
      <a href="#">Directory</a>
      <a href="#">Articles</a>
      <a href="#">Deals</a>
      <a href="#">Forums</a>
      <a href="#">Contact Us</a>
      <a class="register" href="#">Register</a>
    </nav>
  </header>

  <section class="hero">
    <div class="video" role="img" aria-label="Introductory video of the business networking platform">
      <div class="video-play"><svg width="20" height="24" viewBox="0 0 20 24"><path d="M0 0L20 12L0 24Z" fill="#fff"/></svg></div>
      <div class="video-bar">
        <svg width="10" height="12" viewBox="0 0 10 12"><path d="M0 0L10 6L0 12Z" fill="#fff"/></svg>
        <div class="track"><span></span></div>
        <svg width="12" height="10" viewBox="0 0 12 10"><path d="M0 3H3L7 0V10L3 7H0Z" fill="#fff"/></svg>
      </div>
    </div>
    <div class="hero-copy">
      <div class="project"><span class="project-badge"></span><div class="project-name">Sheikh Rashid Al Nadeem<br>Project</div></div>
      <p>An online business networking platform exclusive for UAE Freezone Companies, where they can learn, communicate effectively and benefit from working with each other.</p>
      <a class="btn-register" href="#">REGISTER NOW</a>
    </div>
  </section>

  <section class="welcome">
    <div class="welcome-text">
      <h2>Welcome to Our Website:</h2>
      <p>Lorem Ipsum is simply dummy text of the printing and typesetting industry. Lorem Ipsum has been the industry's standard dummy text ever since the 1500s, when an unknown printer took a galley of type and scrambled it to make a type specimen book.</p>
      <p>It has survived not only five centuries, but also the leap into electronic typesetting, remaining essentially unchanged. It was popularised in the 1960s with the release of Letraset sheets containing Lorem Ipsum passages, and more recently with desktop publishing software like Aldus PageMaker including versions of Lorem Ipsum.</p>
      <a class="read-more" href="#">+ Read More</a>
    </div>
    <div class="welcome-art" role="img" aria-label="Illustration of connected member companies"></div>
  </section>

  <section class="testimonials">
    <h3>What Our Clients Says</h3>
    <p class="quote">“ Lorem Ipsum is simply dummy text of the printing and typesetting industry. It has survived not only five centuries, but also the leap into electronic typesetting including versions of Lorem Ipsum. Lorem Ipsum is simply dummy text of the printing and typesetting industry. It has survived not only five centuries, but also the leap into electronic typesetting including versions of Lorem Ipsum. ”</p>
    <div class="client">Happy Client<span>Designation</span></div>
  </section>

  <section class="partners">
    <div class="partner"><i></i>Northwind</div>
    <div class="partner"><i></i>Solace</div>
    <div class="partner"><i></i>Arcline</div>
    <div class="partner"><i></i>Vireo</div>
    <div class="partner"><i></i>Orbita</div>
    <div class="partner">Meridus</div>
    <div class="partner"><i></i>Kestrel</div>
    <div class="partner">Tallis</div>
    <div class="partner"><i></i>Pinecrest</div>
  </section>

  <footer class="footer">
    <div class="footer-col tweet">
      <h4>Latest Tweet</h4>
      <strong style="color:#fff">Tweet Title</strong>
      <p>Members shared new updates on trade licences, visa renewals and upcoming networking evenings across the free zones this week. Join the conversation and share yours. <a href="#">#HLG</a></p>
      <p><a href="#">2 hours ago</a></p>
    </div>
    <div class="footer-col articles">
      <h4>Latest Article</h4>
      <div class="article"><strong>› Article Title 1</strong>A short guide for new free zone companies on building partnerships with fellow members. <a href="#">› Read More</a></div>
      <div class="article"><strong>› Article Title 2</strong>How members cut costs by sharing logistics and services inside the network. <a href="#">› Read More</a></div>
    </div>
    <div class="footer-col contact">
      <h4>Contact Us</h4>
      <p><svg width="12" height="12" viewBox="0 0 12 12"><path d="M2 1L4 1L5 4L3.5 5Q5 7.5 7 8.5L8 7L11 8V10Q11 11 10 11Q1 10 1 2Q1 1 2 1Z" fill="#bdbdbd"/></svg>+971 (4) 555 0188</p>
      <p><svg width="12" height="10" viewBox="0 0 12 10"><rect x="0.5" y="0.5" width="11" height="9" fill="none" stroke="#bdbdbd"/><path d="M0.5 0.5L6 5.5L11.5 0.5" fill="none" stroke="#bdbdbd"/></svg>info@harborlinkguild.ae</p>
      <h4 style="margin-top:14px">Connect with us</h4>
      <div class="socials"><i></i><i></i><i></i><i></i><i></i></div>
    </div>
  </footer>
  <div class="bottom-bar">
    <span>© 2014 Harbor Link Guild. All rights reserved.</span>
    <nav><a href="#">Home</a> | <a href="#">About HLG</a> | <a href="#">Contact HGL</a> | <a href="#">Terms &amp; Conditions</a> | <a href="#">Privacy</a></nav>
  </div>
</div>
</body>
</html>
```